Autodetailing namecard design: Rose Gold Lettering on Black Matt

This is a namecard design project
requiring two-sided design
Base Color of Namecard: black matt

On front:
Company name,
"Lumina Finishes 14 Cendana"
Subtext: Auto Detailing Studio

Name of card holder: Marcus Oyelaran
Phone Number: +6011-4837-5062
address: 14, Jalan Cendana 5/3Taman Seri Cendana, 81400 Johor Bahru, Johor, Malaysia

Back:
Our Services
High Gloss Car Paint Protection
Custom Color Modification and Styling
Anti-Chip Glass Protection Film
Heat Rejection Glass Tinting

Target Market(s)

Autodetailing for highend cars

Contact Information for Business Card

as mentioned in project details

Colors

Designer to choose colors to be used in the design.

Requirements
Must have
• The main value-add to this project is the design of a logo suited for our purpose and name, and the inclusion of business card details into the card design

```html
<!DOCTYPE html>
<html lang="en">
<head>
<meta charset="utf-8">
<title>Lumina Finishes 14 Cendana – Name Card</title>
<link href="https://fonts.googleapis.com/css2?family=Roboto:wght@400;500;700&family=Exo+2:wght@600&display=swap" rel="stylesheet">
<style>
  :root {
    --backdrop: #686868;
    --card-black: #1f1f1f;
    --card-edge: #2a2a2a;
    --rose-gold: #c8987f;
    --rose-gold-light: #ecc9b6;
    --rose-gold-band: #e4bca6;
    --band-ink: #1d1d1d;
    --contact-ink: #b9b9b9;
  }
  * { box-sizing: border-box; margin: 0; padding: 0; }
  html, body { width: 1200px; height: 568px; overflow: hidden; }
  body {
    background: var(--backdrop);
    position: relative;
    font-family: "Roboto", Arial, sans-serif;
  }
  .card {
    position: absolute;
    top: 154px;
    width: 430px;
    height: 259px;
    border-radius: 11px;
    background: radial-gradient(ellipse at 50% 40%, #262626 0%, var(--card-black) 70%);
    border: 1px solid var(--card-edge);
    overflow: hidden;
  }
  .card--front { left: 140px; }
  .card--back { left: 630px; }

  .brand { position: absolute; color: var(--rose-gold); }
  .brand__name {
    font-weight: 700;
    line-height: 1.1;
    letter-spacing: 0.5px;
  }
  .brand__tagline {
    font-weight: 700;
    text-transform: uppercase;
    letter-spacing: 1.5px;
    margin-top: 6px;
  }
  .card--front .brand {
    left: 0; right: 0; top: 52px;
    text-align: center;
  }
  .card--front .brand__name { font-size: 26px; }
  .card--front .brand__tagline { font-size: 10px; }
  .card--back .brand {
    right: 33px; top: 36px;
    width: 220px;
    text-align: center;
  }
  .card--back .brand__name { font-size: 21px; }
  .card--back .brand__tagline { font-size: 8px; }

  .services {
    position: absolute;
    left: 0; right: 0; top: 181px;
    height: 49px;
    background: linear-gradient(90deg, var(--rose-gold-band), var(--rose-gold-light) 50%, var(--rose-gold-band));
    color: var(--band-ink);
    font-size: 11.5px;
    text-align: center;
    padding-top: 9px;
    line-height: 18px;
  }
  .services__item::before { content: "» "; }
  .services__item + .services__item { margin-left: 6px; }

  .holder {
    position: absolute;
    left: 28px; top: 155px;
  }
  .holder__name {
    font-family: "Exo 2", "Roboto", sans-serif;
    font-weight: 600;
    font-size: 18px;
    color: var(--rose-gold);
    letter-spacing: 0.5px;
    margin-bottom: 10px;
  }
  .holder__line {
    font-size: 11.5px;
    color: var(--contact-ink);
    line-height: 16.5px;
  }
</style>
</head>
<body>
  <section class="card card--front" aria-label="Card front">
    <div class="brand">
      <p class="brand__name">LUMINA FINISHES<br>14 CENDANA</p>
      <p class="brand__tagline">Auto Detailing Studio</p>
    </div>
    <div class="services">
      <p><span class="services__item">High Gloss Car Paint Protection</span><span class="services__item">Custom Color Modification &amp; Styling</span></p>
      <p><span class="services__item">Anti-Chip Glass Protection Film</span><span class="services__item">Heat Rejection Glass Tinting</span></p>
    </div>
  </section>

  <section class="card card--back" aria-label="Card back">
    <div class="brand">
      <p class="brand__name">LUMINA FINISHES<br>14 CENDANA</p>
      <p class="brand__tagline">Auto Detailing Studio</p>
    </div>
    <div class="holder">
      <p class="holder__name">Marcus Oyelaran</p>
      <p class="holder__line">+6011-4837-5062</p>
      <p class="holder__line">14, Jalan Cendana 5/3Taman Seri Cendana,</p>
      <p class="holder__line">81400 Johor Bahru, Johor, Malaysia</p>
    </div>
  </section>
</body>
</html>
```